Wedding Save they date card design

This save the date card must incorporate pinks, rose gold and cream on a white background, the Bride and groom names are Varnett & Lusa, the date for the wedding is July 27th 2018 location Nassau Bahamas

```html
<!DOCTYPE html>
<html lang="en">
<head>
<meta charset="utf-8">
<title>Save the Date – Varnett &amp; Lusa</title>
<link rel="stylesheet" href="https://fonts.googleapis.com/css2?family=Pinyon+Script&display=swap">
<style>
  :root {
    --paper: #f6f4f4;
    --ink: #4a4a4a;
    --blush: #e9a9cb;
    --ornament-a: #f3c6de;
    --ornament-b: #f8e2ee;
  }
  html, body {
    margin: 0;
    padding: 0;
    overflow: hidden;
    background: #ffffff;
  }
  .card {
    position: relative;
    width: 928px;
    height: 1200px;
    background: var(--paper);
    overflow: hidden;
    font-family: "Pinyon Script", cursive;
  }
  .ornament {
    position: absolute;
    background: linear-gradient(160deg, var(--ornament-a), var(--ornament-b));
  }
  .ornament--top { left: 30px; top: 12px; width: 868px; height: 190px; border-radius: 40px 40px 0 0; }
  .ornament--bottom { left: 30px; top: 990px; width: 868px; height: 190px; border-radius: 0 0 40px 40px; }
  .ornament--corner-tl { left: 30px; top: 202px; width: 180px; height: 215px; border-radius: 0 0 60px 30px; }
  .ornament--corner-tr { left: 718px; top: 202px; width: 180px; height: 215px; border-radius: 0 0 30px 60px; }
  .ornament--corner-bl { left: 30px; top: 760px; width: 180px; height: 230px; border-radius: 30px 60px 0 0; }
  .ornament--corner-br { left: 718px; top: 760px; width: 180px; height: 230px; border-radius: 60px 30px 0 0; }
  .ornament--side-l { left: 66px; top: 450px; width: 100px; height: 270px; border-radius: 50px; }
  .ornament--side-r { left: 762px; top: 450px; width: 100px; height: 270px; border-radius: 50px; }

  .line {
    position: absolute;
    left: 0;
    width: 100%;
    margin: 0;
    text-align: center;
    font-weight: 400;
    line-height: 1.2;
    white-space: nowrap;
  }
  .heading { top: 228px; font-size: 66px; color: var(--ink); }
  .date { top: 318px; font-size: 46px; color: var(--ink); }
  .name { font-size: 144px; color: var(--blush); }
  .name--first { top: 408px; }
  .ampersand { top: 560px; font-size: 120px; }
  .name--second { top: 660px; }
  .location { top: 905px; font-size: 42px; color: var(--ink); }
</style>
</head>
<body>
  <main class="card">
    <div class="ornament ornament--top" role="img" aria-label="Pink swirling filigree border along the top edge"></div>
    <div class="ornament ornament--corner-tl" role="img" aria-label="Pink filigree scrollwork, top left corner"></div>
    <div class="ornament ornament--corner-tr" role="img" aria-label="Pink filigree scrollwork, top right corner"></div>
    <div class="ornament ornament--side-l" role="img" aria-label="Pink curling flourish on the left side"></div>
    <div class="ornament ornament--side-r" role="img" aria-label="Pink curling flourish on the right side"></div>
    <div class="ornament ornament--corner-bl" role="img" aria-label="Pink filigree scrollwork, bottom left corner"></div>
    <div class="ornament ornament--corner-br" role="img" aria-label="Pink filigree scrollwork, bottom right corner"></div>
    <div class="ornament ornament--bottom" role="img" aria-label="Pink swirling filigree border along the bottom edge"></div>

    <h1 class="line heading">Save the Date</h1>
    <p class="line date">July 27th 2018</p>
    <p class="line name name--first">Varnett</p>
    <p class="line name ampersand">&amp;</p>
    <p class="line name name--second">Lusa</p>
    <p class="line location">Nassau Bahamas</p>
  </main>
</body>
</html>
```